Bus. Card/Envelope/Letterhead Design Request with my Logo

I have a logo created. I need to create a business card design, letterhead design and envelope design with the new logo.
Updates

The logo has now been posted. Thank you.

Target Market(s)

Professional. Legal Field.

Industry/Entity Type

Business

Requirements
Must have
• I like the same font as the logo.

```html
<!DOCTYPE html>
<html lang="en">
<head>
<meta charset="utf-8">
<title>Carrow Whitfield LLP — Stationery</title>
<link href="https://fonts.googleapis.com/css2?family=Lato:wght@400;700&display=swap" rel="stylesheet">
<style>
  :root{
    --bg:#ececee;
    --paper:#ffffff;
    --ink:#3a3a3c;
    --ink-soft:#7a7a7e;
    --band:#232325;
    --mark:#8a8a8e;
    --orange:#e9a21a;
    --olive:#c8b22a;
    --purple:#675a97;
    --blue:#27a3cb;
    --magenta:#a34b9a;
    --badge-edge:#1f3f7a;
  }
  *{box-sizing:border-box;margin:0;padding:0}
  html,body{width:1200px;height:977px;overflow:hidden;background:var(--bg)}
  body{position:relative;font-family:'Lato',sans-serif;color:var(--ink)}

  .sheet{position:absolute;background:var(--paper);box-shadow:0 2px 8px rgba(0,0,0,.12);overflow:hidden}

  /* colour field standing in for the faceted artwork */
  .artwork{position:absolute;inset:0}
  .artwork--folder{background:linear-gradient(125deg,var(--orange) 0%,var(--olive) 35%,var(--purple) 62%,var(--blue) 100%)}
  .artwork--envelope{background:linear-gradient(115deg,var(--blue) 0%,var(--orange) 30%,var(--purple) 65%,var(--magenta) 100%)}

  /* firm name */
  .firm{position:absolute;display:flex;align-items:center;gap:8px;
    font-family:'Lato',sans-serif;font-weight:400;white-space:nowrap;color:var(--ink)}
  .firm__square{width:10px;height:10px;background:var(--mark);flex:none}
  .firm--light{color:#f2f2f2}

  /* letterhead */
  .letterhead{left:40px;top:40px;width:400px;height:566px}
  .letterhead .firm{right:34px;top:48px;font-size:15px}
  .letterhead__footer{position:absolute;left:34px;right:34px;bottom:34px;display:flex;justify-content:space-between;
    font-size:7.5px;line-height:1.5;color:var(--ink-soft)}
  .letterhead__footer address{font-style:normal}

  /* folder */
  .folder{left:640px;top:40px;width:520px;height:360px}
  .folder .firm{left:50%;top:50%;transform:translate(-50%,-50%);font-size:22px}

  /* envelope */
  .envelope{left:640px;top:430px;width:520px;height:248px}
  .envelope .firm{left:50%;top:62%;transform:translate(-50%,-50%);font-size:17px}

  /* business cards */
  .card{width:280px;height:160px;top:660px}
  .card--front{left:40px}
  .card__band{position:absolute;left:0;right:0;top:52px;height:56px;background:var(--band)}
  .card--front .firm{left:50%;top:80px;transform:translate(-50%,-50%);font-size:12px}

  .card--back{left:340px}
  .card__edge{position:absolute;left:0;top:0;bottom:0;width:8px;background:var(--purple)}
  .card--back .firm{left:22px;top:20px;font-size:10px}
  .card__person{position:absolute;left:22px;bottom:22px;font-size:9px;line-height:1.4}
  .card__person strong{display:block;font-weight:700;letter-spacing:.04em}
  .card__contacts{position:absolute;right:16px;top:64px;list-style:none;font-size:7.5px;color:var(--ink-soft)}
  .card__contacts li{display:flex;align-items:center;gap:6px;margin-bottom:7px}
  .card__icon{width:13px;height:13px;flex:none}

  /* badge */
  .badge{left:640px;top:700px;width:190px;height:250px;border:4px solid var(--badge-edge);border-radius:6px}
  .badge__slot{position:absolute;left:50%;top:10px;width:70px;height:6px;margin-left:-35px;border-radius:3px;background:#d8d8dc}
  .badge__strip{position:absolute;right:0;top:40px;width:14px;height:90px;background:var(--purple)}
  .badge .firm{left:50%;top:55%;transform:translate(-50%,-50%);font-size:11px}
</style>
</head>
<body>

<section class="sheet letterhead" aria-label="Letterhead">
  <div class="firm"><span class="firm__square"></span>Carrow Whitfield LLP</div>
  <footer class="letterhead__footer">
    <address>120 Harbor Street, Suite 400<br>Boston, MA 02110</address>
    <p>T 617 555 0142<br>F 617 555 0143</p>
    <p>info@carrowwhitfield.com<br>carrowwhitfield.com</p>
  </footer>
</section>

<section class="sheet folder" aria-label="Presentation folder">
  <div class="artwork artwork--folder" role="img" aria-label="Multicoloured faceted artwork in orange, yellow, purple and blue"></div>
  <div class="firm"><span class="firm__square"></span>Carrow Whitfield LLP</div>
</section>

<section class="sheet envelope" aria-label="Envelope">
  <div class="artwork artwork--envelope" role="img" aria-label="Multicoloured faceted artwork in blue, orange, purple and magenta"></div>
  <div class="firm"><span class="firm__square"></span>Carrow Whitfield LLP</div>
</section>

<section class="sheet card card--front" aria-label="Business card front">
  <div class="card__band"></div>
  <div class="firm firm--light"><span class="firm__square"></span>Carrow Whitfield LLP</div>
</section>

<section class="sheet card card--back" aria-label="Business card back">
  <div class="card__edge"></div>
  <div class="firm"><span class="firm__square"></span>Carrow Whitfield LLP</div>
  <div class="card__person"><strong>Daniel Reyes</strong>Managing Partner</div>
  <ul class="card__contacts">
    <li>
      <svg class="card__icon" viewBox="0 0 14 14" aria-hidden="true"><circle cx="7" cy="7" r="7" fill="var(--mark)"/><path d="M4.5 3.5l1.5 0 .6 2-1 .8a6 6 0 0 0 2.6 2.6l.8-1 2 .6v1.5a1 1 0 0 1-1 1A6.5 6.5 0 0 1 3.5 4.5a1 1 0 0 1 1-1z" fill="#fff"/></svg>
      617 555 0142
    </li>
    <li>
      <svg class="card__icon" viewBox="0 0 14 14" aria-hidden="true"><circle cx="7" cy="7" r="7" fill="var(--mark)"/><rect x="3.5" y="4.5" width="7" height="5" fill="#fff"/><polyline points="3.5,4.5 7,7.5 10.5,4.5" fill="none" stroke="var(--mark)" stroke-width=".8"/></svg>
      d.reyes@carrowwhitfield.com
    </li>
    <li>
      <svg class="card__icon" viewBox="0 0 14 14" aria-hidden="true"><circle cx="7" cy="7" r="7" fill="var(--mark)"/><path d="M7 3a2.5 2.5 0 0 1 2.5 2.5C9.5 7.5 7 11 7 11S4.5 7.5 4.5 5.5A2.5 2.5 0 0 1 7 3z" fill="#fff"/><circle cx="7" cy="5.5" r=".9" fill="var(--mark)"/></svg>
      120 Harbor Street, Boston
    </li>
  </ul>
</section>

<section class="sheet badge" aria-label="Staff badge">
  <div class="badge__slot"></div>
  <div class="badge__strip"></div>
  <div class="firm"><span class="firm__square"></span>Carrow Whitfield LLP</div>
</section>

</body>
</html>
```